Design for company homepage promoting to the pharmaceutical industry

Our company produces medical education materials and services for the pharmaceutical industry. Our existing website (www.quorvan.net.au) provides more information.
 
We need a homepage design for our new company website we are creating. Our site will not have a great amount of content, we want it to be fast, user friendly and easily adaptable to viewing on any platform, and through any browser. We don't want it over-designed - i.e. no highly animated banner flags, backgrounds, obscure webfonts, too many graphics etc. Attached are files indicating our existing company logo and design. We want the logo and rings to be retained. We've also attached draft copy for the website.
The final website may be designed in Wordpress (still to be confirmed)
 
This is a design to replace the current site (www.quorvan.net.au). Content will also be revised.
Things we don't like about our current design - doesn't use our current branding, is not very exciting, old fashioned 'standard' format, too much content, just doesn't look that good, boring.
 
Examples of sites we like:
www.brelmot.com.au
http://factsheets.wondipaq.com.au/index.html
 
Features we like from these sites - fast, responsive, short and to the point, cross-platform compatible including smartphones, and looks good
 
Main reasons people will visit our site: to find out whether we can provide services they might be looking for, to make a decision on whether they are interested in what we offer so they can get in touch with us, and to get our contact details.
Main thing we want to achieve from website visits is that it looks good enough and provides enough summary information on us so that they want to get in touch with us, to offer us work or to ask us to come in and meet them to provide more info on what we do.
Two most important calls to action from our website
· make the decision that we can do what you are looking for
· get in touch with us.
Updates

Thanks everyone for your submissions. At this stage with the Christmas break upon us, we are yet to finalise our decision, and will make a decision early in the new year. I hope everyone has a good holiday break.
Kind regards
Doug

Target Market(s)

Pharmaceutical industry professionals, marketers and medical professionals.

Industry/Entity Type

Pharmaceutical

Requirements
Must have
• Company logo and rings must be incorporated, company colour - blue - must be in there.
Should not have
• Complex animation or graphics that will slow the upload or limit cross-platform compatability/viewing on smartphones etc.

```html
<!DOCTYPE html>
<html lang="en">
<head>
<meta charset="utf-8">
<title>Quorvan Healthcare Education</title>
<link href="https://fonts.googleapis.com/css2?family=Open+Sans:wght@400;600;700&family=Oswald:wght@500;700&family=Bebas+Neue&display=swap" rel="stylesheet">
<style>
:root{
  --blue:#0a9fd8;
  --navy:#1b5d9c;
  --ink:#2b6797;
  --band:#bfe1f1;
  --pale:#e8f3f8;
  --navbg:#d9edf7;
  --box:#dfecf1;
  --line:#c5dbe4;
  --white:#fff;
  --grey:#555;
}
*{margin:0;padding:0;box-sizing:border-box}
html,body{width:1200px;height:2719px;overflow:hidden}
body{position:relative;font-family:"Open Sans",Arial,sans-serif;background:var(--white);color:var(--ink)}
.abs{position:absolute}
/* header */
.header{left:0;top:0;width:1200px;height:141px;background:var(--white)}
.brand{left:30px;top:22px;display:flex;align-items:flex-end;gap:12px}
.brand-name{font-size:68px;font-weight:600;color:var(--navy);line-height:1;letter-spacing:-1px}
.brand-dot{width:14px;height:14px;border-radius:50%;background:var(--blue);margin-bottom:10px}
.brand-sub{left:56px;top:96px;font-size:12px;font-weight:600;color:var(--navy);letter-spacing:1px}
.head-phone{right:34px;top:56px;display:flex;align-items:center;gap:10px}
.head-phone .lbl{position:absolute;right:0;top:-2px;font-size:15px;color:var(--navy);white-space:nowrap}
.head-phone .num{font-family:"Oswald",sans-serif;font-weight:700;font-size:31px;color:var(--blue);margin-top:16px;line-height:1}
/* nav */
.nav{left:0;top:141px;width:1200px;height:51px;background:var(--navbg);display:flex;font-size:17px;color:var(--navy)}
.nav a{color:inherit;text-decoration:none;display:block;line-height:51px;position:absolute}
.nav a.active{background:var(--blue);color:var(--white);width:129px;text-align:center;left:0}
/* sections */
.sec{left:0;width:1200px}
.s-intro{top:192px;height:723px;background:var(--band)}
.s-about{top:915px;height:648px;background:var(--pale)}
.s-clients{top:1563px;height:429px;background:var(--band)}
.s-contact{top:1992px;height:646px;background:var(--pale)}
.s-foot{top:2638px;height:81px;background:var(--band)}
.title{width:1200px;left:0;text-align:center;font-family:"Bebas Neue",sans-serif;font-size:46px;color:var(--navy);line-height:1}
.sub{width:1200px;left:0;text-align:center;font-size:14px;line-height:17px;color:var(--ink)}
.feature .ic{width:116px;height:116px;border-radius:50%;background:var(--pale);display:flex;align-items:center;justify-content:center;position:absolute;left:0;top:0}
.feature h3{position:absolute;left:146px;top:12px;font-family:Arial,sans-serif;font-weight:400;font-size:23px;color:var(--navy)}
.feature p{position:absolute;left:146px;top:44px;width:330px;font-size:17px;line-height:17px;color:var(--ink)}
.lead{left:0;width:1200px;text-align:center;font-family:Arial,sans-serif;font-size:30px;line-height:30px;color:var(--blue)}
.note{background:var(--box);border:1px solid var(--line);border-radius:3px;font-size:14px;line-height:17px;color:#3a3a3a;padding:16px 18px}
.note.center{background:var(--pale);font-size:17px;line-height:20px;padding:24px 40px}
.conn{background:var(--line)}
.quote{font-size:18px;line-height:19px;color:var(--navy)}
.quote p{margin-bottom:14px}
.heading2{left:0;width:1200px;text-align:center;font-family:Arial,sans-serif;font-size:30px;color:var(--blue)}
.addr{left:44px;top:2140px;font-family:Arial,sans-serif;color:var(--ink)}
.addr strong{display:block;font-weight:400;font-size:22px;margin-bottom:4px}
.addr span{font-size:17px;line-height:22px;display:block}
.field{left:38px;width:417px;background:var(--white);border:1px solid var(--line);border-radius:3px;font-size:15px;color:#888;padding:8px 12px}
.submit{left:38px;top:2531px;width:178px;height:43px;background:#6bbcd7;color:var(--white);font-family:Arial,sans-serif;font-size:22px;text-align:center;line-height:43px}
.ct-phone{left:662px;top:2148px;display:flex;align-items:center;gap:12px}
.ct-phone .num{font-family:"Oswald",sans-serif;font-weight:500;font-size:40px;color:#4f7a94}
.map{left:658px;top:2230px;width:499px;height:344px;background:linear-gradient(135deg,#e6e3dc,#d8d5cc 55%,#e9e5dd)}
.foot-links{left:38px;top:2660px;font-size:14px;color:var(--blue)}
.copy{left:38px;top:2687px;font-size:12px;color:var(--blue)}
.social{top:2651px;width:54px;height:54px;border-radius:50%;background:#3f8fc6}
</style>
</head>
<body>

<header class="abs header">
  <div class="abs brand"><span class="brand-name">quorvan</span><span class="brand-dot"></span></div>
  <div class="abs brand-sub">HEALTHCARE EDUCATION</div>
  <div class="abs head-phone">
    <span class="lbl">For Inquiries Contact Us</span>
    <svg width="56" height="56" viewBox="0 0 56 56"><circle cx="28" cy="28" r="25" fill="none" stroke="var(--navy)" stroke-width="4"/><path d="M19 15c3-2 5 3 6 6 1 2-2 3-1 5 2 4 4 6 8 8 2 1 3-2 5-1 3 1 8 3 6 6-2 4-6 5-10 3-7-3-13-9-16-16-2-4-1-9 2-11z" fill="var(--navy)"/></svg>
    <span class="num">+61 2 9555 0184</span>
  </div>
</header>

<nav class="abs nav">
  <a class="active" href="#">Home</a>
  <a href="#" style="left:166px">Who We Are</a>
  <a href="#" style="left:340px">What We Do</a>
  <a href="#" style="left:515px">Clients</a>
  <a href="#" style="left:644px">Work</a>
  <a href="#" style="left:762px">Testimonials</a>
  <a href="#" style="left:938px">Contact Us</a>
  <a href="#" style="left:1101px">Login</a>
</nav>

<section class="abs sec s-intro">
  <h1 class="abs title" style="top:64px">Welcome to Quorvan Healthcare Education</h1>
  <p class="abs sub" style="top:107px">Quorvan have developed a unique tool for the online management of drug delivery,<br>ideal for implementation in early access andspecial needs programs.</p>

  <div class="abs feature" style="left:53px;top:183px">
    <div class="ic"><svg width="70" height="50" viewBox="0 0 70 50"><rect x="12" y="4" width="46" height="32" rx="2" fill="var(--navy)"/><rect x="16" y="8" width="38" height="24" fill="#2f86c9"/><path d="M2 40h66l-4 6H6z" fill="var(--navy)"/><path d="M36 16l8 8-3 1 2 4-2 1-2-4-3 2z" fill="#fff"/></svg></div>
    <h3>Promotion</h3>
    <p>Quorvan can help you promote your brand – from the development of strategic communication campaigns .</p>
  </div>
  <div class="abs feature" style="left:653px;top:183px">
    <div class="ic"><svg width="60" height="64" viewBox="0 0 60 64"><rect x="24" y="4" width="10" height="30" rx="2" transform="rotate(-25 29 19)" fill="var(--navy)"/><path d="M38 30a16 16 0 0 1-6 24" fill="none" stroke="var(--navy)" stroke-width="5"/><rect x="10" y="54" width="40" height="6" fill="var(--navy)"/><rect x="18" y="36" width="18" height="6" fill="var(--navy)"/></svg></div>
    <h3>Education</h3>
    <p>Clinical papers, evidence summaries, scientific newsletters and accredited educational materials.</p>
  </div>
  <div class="abs feature" style="left:53px;top:354px">
    <div class="ic"><svg width="62" height="56" viewBox="0 0 62 56"><rect x="4" y="4" width="40" height="12" fill="var(--navy)"/><rect x="4" y="20" width="40" height="12" fill="var(--navy)"/><rect x="4" y="36" width="26" height="12" fill="var(--navy)"/><rect x="30" y="28" width="28" height="24" fill="#fff" stroke="var(--navy)" stroke-width="3"/><path d="M35 36h18M35 42h18M35 48h12" stroke="var(--navy)" stroke-width="2"/></svg></div>
    <h3>Programs</h3>
    <p>Clinical papers, evidence summaries, scientific newsletters and accredited educational materials.</p>
  </div>
  <div class="abs feature" style="left:653px;top:354px">
    <div class="ic"><svg width="72" height="50" viewBox="0 0 72 50"><circle cx="20" cy="14" r="8" fill="var(--navy)"/><circle cx="52" cy="14" r="8" fill="var(--navy)"/><circle cx="36" cy="18" r="10" fill="var(--navy)"/><path d="M6 40c0-10 8-14 14-14s8 2 8 2M66 40c0-10-8-14-14-14s-8 2-8 2" fill="var(--navy)"/><path d="M18 46c0-12 8-17 18-17s18 5 18 17z" fill="var(--navy)"/></svg></div>
    <h3 style="font-size:27px;top:8px">Meetings</h3>
    <p>You will maximise your investment in scientific meetings by employing Quorvan to manage the entire process.</p>
  </div>
  <div class="abs feature" style="left:53px;top:524px">
    <div class="ic"><svg width="50" height="64" viewBox="0 0 50 64"><path d="M18 14h14v14l14 26c2 4 0 6-4 6H8c-4 0-6-2-4-6l14-26z" fill="none" stroke="var(--navy)" stroke-width="4"/><path d="M11 44h28l5 10c1 2 0 3-2 3H8c-2 0-3-1-2-3z" fill="#2f86c9"/><circle cx="26" cy="6" r="3" fill="var(--navy)"/><circle cx="31" cy="2" r="2" fill="var(--navy)"/></svg></div>
    <h3>IME</h3>
    <p>In an environment of ever-increasing scrutiny over the support that pharmaceutical companies.</p>
  </div>
</section>

<section class="abs sec s-about">
  <p class="abs lead" style="top:94px">At Quorvan we are healthcare communication specialists;<br>this means we’re scientists, journalists and marketers rolled into one.</p>
  <div class="abs conn" style="left:245px;top:1178px;width:63px;height:2px;margin-top:-915px"></div>
  <div class="abs conn" style="left:877px;top:263px;width:76px;height:2px"></div>
  <div class="abs conn" style="left:421px;top:374px;width:2px;height:67px"></div>
  <div class="abs conn" style="left:764px;top:374px;width:2px;height:67px"></div>
  <div class="abs note" style="left:18px;top:209px;width:227px;height:120px">Strategic tools for brand promotion (such as detail aids, product monographs, slide kits and patient materials)</div>
  <div class="abs note center" style="left:308px;top:209px;width:569px;height:165px">As you can see we provide all the things you’d expect from a top-class healthcare communications agency, but we have the depth of technical understanding and creative flair to produce sophisticated and memorable materials and programs, including:</div>
  <div class="abs note" style="left:953px;top:209px;width:227px;height:120px">Non-promotional materials for market education (e.g. clinical papers and evidence summaries)</div>
  <div class="abs note" style="left:308px;top:441px;width:227px;height:85px">Complex programs such as clinical audits and product familiarisation programs</div>
  <div class="abs note" style="left:651px;top:441px;width:226px;height:85px;padding-top:22px">Medical meetings and symposia</div>
</section>

<section class="abs sec s-clients">
  <h2 class="abs title" style="top:62px">What Clients Say</h2>
  <p class="abs sub" style="top:107px">Want to speak to a referee directly? <strong style="color:#1a2a3a">Email Us</strong> and we will make the arrangements.</p>
  <svg class="abs" style="left:36px;top:195px" width="106" height="95" viewBox="0 0 106 95"><path d="M22 14h-14v46h10v16l16-16h30" fill="none" stroke="var(--navy)" stroke-width="5"/><rect x="22" y="4" width="78" height="56" rx="8" fill="none" stroke="var(--navy)" stroke-width="6"/><path d="M36 20h14M56 20h30M36 32h30M72 32h14M36 44h22M64 44h22" stroke="var(--navy)" stroke-width="4"/><path d="M60 60l16 16V60" fill="var(--navy)"/></svg>
  <div class="abs quote" style="left:172px;top:195px;width:375px">
    <p>“Congratulations &amp; many thanks for your seriously wonderful &amp; successful work on the weekend. I’m especially grateful for the calm, cool &amp; very clever work done in managing all the planning process before I even came on board – truly outstanding”</p>
    <p>“Thank you for all your help with making the meeting the huge success that it was”</p>
  </div>
  <svg class="abs" style="left:627px;top:195px" width="106" height="95" viewBox="0 0 106 95"><path d="M22 14h-14v46h10v16l16-16h30" fill="none" stroke="var(--navy)" stroke-width="5"/><rect x="22" y="4" width="78" height="56" rx="8" fill="none" stroke="var(--navy)" stroke-width="6"/><path d="M36 20h14M56 20h30M36 32h30M72 32h14M36 44h22M64 44h22" stroke="var(--navy)" stroke-width="4"/><path d="M60 60l16 16V60" fill="var(--navy)"/></svg>
  <div class="abs quote" style="left:762px;top:195px;width:395px">
    <p style="padding-left:8px">“Your organisation of the speakers in the lead-up to the event and on the day left nothing to chance”</p>
    <p>“The manner with which Quorvan produced the invitations and P and A booklet with tight timelines, to such a high quality, is tremendous”</p>
  </div>
</section>

<section class="abs sec s-contact">
  <h2 class="abs heading2" style="top:74px">Know more about Us. Contact Us</h2>
</section>
<div class="abs addr"><strong>Quorvan Healthcare Education</strong><span>Level 4, 18 Wattle Street, North Sydney NSW 2060</span><span>Australia</span></div>
<div class="abs field" style="top:2232px;height:38px">Full Name</div>
<div class="abs field" style="top:2280px;height:38px">Email</div>
<div class="abs field" style="top:2329px;height:38px">Telephone</div>
<div class="abs field" style="top:2378px;height:133px">Message</div>
<div class="abs submit">SUBMIT</div>
<div class="abs ct-phone">
  <svg width="60" height="60" viewBox="0 0 56 56"><circle cx="28" cy="28" r="25" fill="none" stroke="#4f7a94" stroke-width="4"/><path d="M19 15c3-2 5 3 6 6 1 2-2 3-1 5 2 4 4 6 8 8 2 1 3-2 5-1 3 1 8 3 6 6-2 4-6 5-10 3-7-3-13-9-16-16-2-4-1-9 2-11z" fill="#4f7a94"/></svg>
  <span class="num">+61 2 9555 0184</span>
</div>
<div class="abs map" role="img" aria-label="Street map showing the office location in North Sydney"></div>

<footer class="abs sec s-foot"></footer>
<div class="abs foot-links">Home · Who We Are · What We Do · Clients · Work · Testimonials · Contact Us · Login</div>
<div class="abs copy">© Copyright 2013 Quorvan. All Rights Reserved</div>
<div class="abs social" style="left:840px" aria-label="Social link"></div>
<div class="abs social" style="left:909px" aria-label="Social link"></div>
<div class="abs social" style="left:980px" aria-label="Social link"></div>
<div class="abs social" style="left:1050px" aria-label="Social link"></div>
<div class="abs social" style="left:1120px" aria-label="Social link"></div>

</body>
</html>
```